DL size flyer design for renovations and extensions construction company

We are looking for a flyer design for a construction company specialising in renovations, extensions, and minor building works. The aim is for anyone needing any home construction works to pick up the phone and call us. The flyers will be delivered primarily to letterboxes of homes. We want the flyers to stick out from all the other things people get in the mail by any means possible.

Target Market(s)

The audience we target is residential home owners and are looking to deliver these letters to home letterboxes.

Industry/Entity Type

Residential Construction

Font styles to use
Sans Serif

Colors
000000
ffffff

Requirements
Must have
• 1 - Places for 4 photos with descriptions reading: (1) Bathroom Renovations (4) Kitchen Renovations (3) Home Extensions (4) Outdoor works and landscaping. This may be on the reverse side of the DL flyer.
• 2 - Fonts to be used are (1) Brandon Grotesque (All caps) for main heading, (2) Montserrat SemiBold (All caps) for Headings, (3) Lato for text.
• 3 - Copy of the finished document in PDF and indesign formats.
• 4 - Placeholders for copy (look at the pelvaridge.com website for now)
Nice to have
• A modern looking design.
Should not have
• Not all photos attached are necessarily required. Up to you to use your creativity to decide on the best combination.

```html
<!DOCTYPE html>
<html lang="en">
<head>
<meta charset="utf-8">
<title>Pelvaridge DL Flyer – Front and Reverse</title>
<link rel="stylesheet" href="https://fonts.googleapis.com/css2?family=Montserrat:wght@300;600;800&family=Lato:wght@400;700&display=swap">
<style>
  :root{
    --black:#000000;
    --white:#ffffff;
    --green:#1f9a5f;
    --green-bright:#23b26b;
    --paper:#f4f4f2;
    --stage:#e6e6e6;
    --ink:#1c1c1c;
  }
  *{box-sizing:border-box;margin:0;padding:0}
  html,body{width:903px;height:1200px;overflow:hidden}
  body{background:var(--stage);position:relative;font-family:"Lato",sans-serif;color:var(--ink)}

  .flyer{position:absolute;top:155px;width:420px;height:890px;background:var(--white);overflow:hidden;box-shadow:0 4px 14px rgba(0,0,0,.12)}
  .flyer--front{left:21px}
  .flyer--reverse{left:462px;background:var(--paper)}
  .shapes{position:absolute;inset:0;width:100%;height:100%}

  /* front */
  .brand{position:absolute;top:28px;left:26px;display:flex;align-items:center;gap:8px;font-family:"Lato",sans-serif;font-weight:700;font-size:28px;letter-spacing:2px;color:var(--black)}
  .brand__mark{width:14px;height:14px;background:var(--green)}
  .hero-photo{position:absolute;top:80px;left:0;width:420px;height:560px;
    background:linear-gradient(180deg,#9aa5ad 0%,#c9cfd3 25%,#8a9488 50%,#5f7a45 75%,#486a33 100%)}
  .headline{position:absolute;top:654px;left:0;width:420px;text-align:center;font-family:"Montserrat",sans-serif;font-weight:800;text-transform:uppercase;color:var(--white);font-size:26px;line-height:1.08;letter-spacing:.5px}
  .headline__accent{color:var(--green-bright)}
  .tagline{position:absolute;top:780px;left:0;width:420px;text-align:center;font-family:"Montserrat",sans-serif;font-weight:600;font-size:12px;line-height:1;letter-spacing:3px;color:var(--white);text-transform:uppercase}
  .web{position:absolute;left:0;width:420px;text-align:center;font-family:"Lato",sans-serif;font-size:15px;letter-spacing:2px;color:var(--white)}
  .flyer--front .web{top:845px}

  /* reverse */
  .services-title{position:absolute;top:26px;left:190px;width:220px;text-align:center;font-family:"Montserrat",sans-serif;font-weight:300;font-size:32px;letter-spacing:3px;color:var(--white);text-transform:uppercase}
  .service__heading{position:absolute;height:40px;display:flex;align-items:center;font-family:"Montserrat",sans-serif;font-weight:600;font-size:13px;line-height:1.1;text-transform:uppercase;color:var(--white);letter-spacing:.5px}
  .service__heading--left{left:16px;width:200px}
  .service__heading--right{left:232px;width:180px}
  .service__text{position:absolute;width:206px;font-size:9.4px;line-height:1.3;color:var(--ink)}
  .service__text p+p{margin-top:5px}
  .service__photo{position:absolute;width:178px;height:150px}
  .photo--bath{background:linear-gradient(160deg,#e9e9e6,#b9bcbc 60%,#8d9090)}
  .photo--kitchen{background:linear-gradient(160deg,#f1efe9,#cfc8bb 55%,#9f9481)}
  .photo--extension{background:linear-gradient(160deg,#efe9e1,#c9a98a 55%,#6b5a4a)}
  .photo--outdoor{background:linear-gradient(180deg,#9fb58c,#5d8a3c 55%,#7a4a2e)}
  .flyer--reverse .web{top:852px;color:var(--white)}
</style>
</head>
<body>

<!-- FRONT -->
<section class="flyer flyer--front">
  <div class="hero-photo" role="img" aria-label="Photo of a modern two-storey rear extension with large glazing and a green garden"></div>
  <svg class="shapes" viewBox="0 0 420 890" aria-hidden="true">
    <rect x="0" y="0" width="420" height="80" fill="var(--white)"/>
    <polygon points="300,80 420,80 420,160" fill="var(--green)"/>
    <polygon points="250,80 300,80 420,160 420,190" fill="var(--black)"/>
    <polygon points="0,540 60,580 0,620" fill="var(--green)"/>
    <polygon points="0,560 110,560 150,630 0,630" fill="var(--green)"/>
    <polygon points="0,620 150,620 190,640 420,640 420,890 0,890" fill="var(--black)"/>
    <polygon points="0,812 380,812 420,790 420,890 0,890" fill="var(--green)"/>
    <polygon points="350,620 420,585 420,640" fill="var(--green)"/>
  </svg>
  <div class="brand"><span class="brand__mark"></span>PELVARIDGE</div>
  <h1 class="headline">Looking<br>to make your<br><span class="headline__accent">home bigger</span><br>or better</h1>
  <p class="tagline">Build · Renovate · Extend</p>
  <p class="web">www.pelvaridge.com</p>
</section>

<!-- REVERSE -->
<section class="flyer flyer--reverse">
  <svg class="shapes" viewBox="0 0 420 890" aria-hidden="true">
    <polygon points="0,0 140,0 100,60 0,60" fill="var(--green)"/>
    <polygon points="170,0 420,0 420,92 130,92 170,40" fill="var(--black)"/>
    <polygon points="0,112 210,112 226,152 0,152" fill="var(--black)"/>
    <polygon points="222,310 420,310 420,350 206,350" fill="var(--black)"/>
    <polygon points="0,470 130,470 110,488 0,488" fill="var(--green)"/>
    <polygon points="0,488 210,488 226,528 0,528" fill="var(--black)"/>
    <polygon points="222,672 420,672 420,712 206,712" fill="var(--black)"/>
    <polygon points="0,664 60,664 0,700" fill="var(--green)"/>
    <polygon points="0,832 420,832 420,890 0,890" fill="var(--black)"/>
    <polygon points="0,812 70,812 40,832 0,850" fill="var(--green)"/>
    <polygon points="350,832 420,800 420,832" fill="var(--green)"/>
  </svg>

  <h2 class="services-title">Services</h2>

  <h3 class="service__heading service__heading--left" style="top:112px">Bathroom<br>Renovations</h3>
  <div class="service__text" style="top:160px;left:14px">
    <p>We create custom bathroom renovations of various shapes and sizes to suit a variety of family needs.</p>
    <p>When considering a bathroom design you will need to take into account a variety of factors including the size of the existing space and whether it can be enlarged, how many people in your family will use the bathroom, if your family size is likely to increase, where the bathroom is located in the home as well as many other considerations.</p>
  </div>
  <div class="service__photo photo--bath" style="top:120px;left:232px" role="img" aria-label="Photo of a bright renovated bathroom with glass shower"></div>

  <div class="service__photo photo--kitchen" style="top:310px;left:12px" role="img" aria-label="Photo of a modern white kitchen"></div>
  <h3 class="service__heading service__heading--right" style="top:310px">Kitchen<br>Renovations</h3>
  <div class="service__text" style="top:358px;left:204px">
    <p>Today's kitchens go further than places to just make a meal – they are the open-plan hub for the modern home.</p>
    <p>Each kitchen will need to work in with each family's unique needs. That's why it's important to work in with an expert designer and builder on your renovation project.</p>
  </div>

  <h3 class="service__heading service__heading--left" style="top:488px">Home<br>Extensions</h3>
  <div class="service__text" style="top:536px;left:14px">
    <p>Structural alteration or extensions are an essential consideration when things simply won't fit or you want to make your home bigger or better.</p>
    <p>Pelvaridge are licenced builders experienced in delivering structural alterations or home extensions and we are always guided by our qualified engineers.</p>
  </div>
  <div class="service__photo photo--extension" style="top:496px;left:232px" role="img" aria-label="Photo of an open-plan extension with dining area and pendant lights"></div>

  <div class="service__photo photo--outdoor" style="top:668px;left:12px" role="img" aria-label="Photo of a landscaped garden with timber bench and lawn"></div>
  <h3 class="service__heading service__heading--right" style="top:672px">Outdoor works and<br>landscaping</h3>
  <div class="service__text" style="top:720px;left:204px">
    <p>Home living spans across both internal and external environments so consider complete home enhancement and integration into the surrounding land. Whether it be landscaping works, pools or outdoor buildings, we design both large scale and compact.</p>
  </div>

  <p class="web">www.pelvaridge.com</p>
</section>

</body>
</html>
```